Priority Goals poster for school year

We are an elementary school and the past two years have had you help us to design a "poster" that illustrates our goal of the coming year. I am attaching our last year's one, along with some photos of our (ver rough) thinking for next years. The priority goal at top remains the same. Can't wait to see your genius ideas! :)

Target Market(s)

Staff of an elementary school and parents to some (informative) extent as well.

Colors
296eb1
6094c6
fbed22
fbee3f

Requirements
Must have
• items from the white board picture we have attached

```html
<!DOCTYPE html>
<html lang="en">
<head>
<meta charset="utf-8">
<title>The Big Picture 2021-2022 – Cedar Ridge Elementary School</title>
<link rel="stylesheet" href="https://fonts.googleapis.com/css2?family=Anton&family=Oswald:wght@500;600;700&family=Open+Sans:wght@600;700&display=swap">
<style>
  :root {
    --blue: #296eb1;
    --light-blue: #78a9d9;
    --navy: #3a4799;
    --yellow: #eecb2e;
    --ink: #2b2b2b;
    --panel: #e6e7e9;
    --line: #a9aaac;
    --white: #ffffff;
  }
  html, body { margin: 0; padding: 0; overflow: hidden; background: var(--white); }
  .poster { display: block; width: 849px; height: 1200px; }
  .title { font-family: "Anton", sans-serif; }
  .cond { font-family: "Oswald", sans-serif; font-weight: 600; }
  .cond-bold { font-family: "Oswald", sans-serif; font-weight: 700; }
  .lede { font-family: "Open Sans", sans-serif; font-weight: 700; }
  .route { fill: none; stroke: var(--line); stroke-width: 5; }
  .node { fill: var(--line); }
  .placeholder { fill: #c7c8ca; }
</style>
</head>
<body>
<svg class="poster" viewBox="0 0 1624 2296" xmlns="http://www.w3.org/2000/svg">
  <!-- background panels -->
  <rect class="canvas" x="0" y="0" width="1624" height="2296" fill="var(--white)"/>
  <rect class="content-panel" x="0" y="520" width="1624" height="1580" fill="var(--panel)"/>
  <path class="name-plate" d="M1045 400 H1624 V565 H1095 Q1045 565 1045 515 Z" fill="var(--white)"/>
  <rect class="footer-rule" x="0" y="2100" width="1624" height="30" fill="var(--yellow)"/>
  <rect class="footer-band" x="0" y="2130" width="1624" height="166" fill="var(--navy)"/>

  <!-- header -->
  <g class="header">
    <rect x="0" y="100" width="1140" height="146" fill="var(--blue)"/>
    <rect x="255" y="45" width="318" height="200" fill="var(--blue)"/>
    <text class="title" x="80" y="228" font-size="140" fill="var(--white)" textLength="180" lengthAdjust="spacingAndGlyphs">THE</text>
    <text class="title" x="290" y="225" font-size="185" fill="var(--yellow)" textLength="240" lengthAdjust="spacingAndGlyphs">BIG</text>
    <text class="title" x="570" y="228" font-size="140" fill="var(--white)" textLength="430" lengthAdjust="spacingAndGlyphs">PICTURE</text>
    <text class="cond-bold" x="232" y="325" font-size="86" fill="var(--blue)" textLength="358" lengthAdjust="spacingAndGlyphs">2021-2022</text>
    <rect x="0" y="340" width="1140" height="12" fill="var(--navy)"/>
    <rect x="0" y="352" width="1140" height="31" fill="var(--yellow)"/>
    <text class="lede" x="78" y="440" font-size="34" fill="var(--navy)" textLength="907" lengthAdjust="spacingAndGlyphs">Steadily maintaining the GROWTH pace, taking small</text>
    <text class="lede" x="78" y="490" font-size="34" fill="var(--navy)" textLength="825" lengthAdjust="spacingAndGlyphs">and measured STEPS towards our higher goals...</text>
  </g>

  <!-- school name -->
  <g class="school-name">
    <circle cx="1330" cy="220" r="130" fill="var(--navy)"/>
    <text class="cond-bold" x="1312" y="460" font-size="78" fill="var(--navy)" text-anchor="middle" textLength="460" lengthAdjust="spacingAndGlyphs">CEDAR RIDGE</text>
    <text class="cond-bold" x="1312" y="505" font-size="40" fill="var(--navy)" text-anchor="middle" textLength="468" lengthAdjust="spacingAndGlyphs">ELEMENTARY SCHOOL</text>
  </g>

  <!-- connecting routes -->
  <g class="routes">
    <path class="route" d="M160 520 V885"/>
    <circle class="node" cx="160" cy="887" r="15"/>
    <path class="route" d="M133 1005 V603 H762"/>
    <path class="route" d="M633 1132 H687 V968 L920 650 H1193 V698"/>
    <circle class="node" cx="97" cy="1132" r="15"/>
    <path class="route" d="M240 1132 H97 V1325 H517 V1575 H660 V1770 H145 V1825 H728"/>
    <circle class="node" cx="728" cy="1825" r="15"/>
    <path class="route" d="M1193 1005 V1080 H1460 Q1505 1080 1505 1125 V1290 Q1505 1335 1460 1335 H870 Q828 1335 828 1293 V1175"/>
    <circle class="node" cx="1193" cy="1037" r="15"/>
    <path class="route" d="M790 1560 V1768 H932 V1885 H1452"/>
    <circle class="node" cx="1452" cy="1885" r="15"/>
  </g>

  <!-- illustration slots -->
  <rect class="placeholder" x="730" y="595" width="122" height="115" rx="10" role="img" aria-label="Icon of a speaker at a podium"/>
  <rect class="placeholder" x="150" y="920" width="165" height="185" rx="10" role="img" aria-label="Icon of a person climbing stairs"/>
  <rect class="placeholder" x="690" y="1430" width="235" height="145" rx="20" role="img" aria-label="Icon of a handshake"/>
  <circle class="placeholder" cx="1472" cy="1770" r="82" role="img" aria-label="Icon of a person with arms outstretched for wellness"/>

  <!-- voices of all -->
  <g class="voices">
    <path d="M335 635 H658 Q718 635 718 695 V870 L685 920 V872 H335 Q275 872 275 812 V695 Q275 635 335 635 Z" fill="var(--blue)"/>
    <text class="cond-bold" x="318" y="722" font-size="70" fill="var(--yellow)" textLength="240" lengthAdjust="spacingAndGlyphs">Voices of</text>
    <rect x="570" y="660" width="107" height="68" fill="var(--yellow)"/>
    <text class="cond-bold" x="580" y="720" font-size="62" fill="var(--ink)" textLength="88" lengthAdjust="spacingAndGlyphs">ALL</text>
    <text class="cond" x="322" y="778" font-size="42" fill="var(--white)" textLength="215" lengthAdjust="spacingAndGlyphs">Who are WE?</text>
    <text class="cond" x="322" y="832" font-size="42" fill="var(--white)" textLength="353" lengthAdjust="spacingAndGlyphs">Where are WE going?</text>
  </g>

  <!-- intentional focus -->
  <g class="intentional">
    <path d="M975 698 H1430 Q1485 698 1485 753 V900 A78 78 0 0 0 1365 1005 H975 Q920 1005 920 950 V753 Q920 698 975 698 Z" fill="var(--yellow)"/>
    <text class="cond-bold" x="972" y="795" font-size="64" fill="var(--navy)" textLength="490" lengthAdjust="spacingAndGlyphs">Be INTENTIONAL with</text>
    <text class="cond-bold" x="972" y="855" font-size="64" fill="var(--navy)" textLength="450" lengthAdjust="spacingAndGlyphs">path and actions...</text>
    <rect x="1076" y="873" width="238" height="117" fill="var(--ink)"/>
    <text class="cond-bold" x="1090" y="970" font-size="110" fill="var(--white)" textLength="210" lengthAdjust="spacingAndGlyphs">focus</text>
    <g class="target-icon" fill="none" stroke="var(--line)" stroke-width="14">
      <circle cx="1443" cy="970" r="60"/>
      <circle cx="1443" cy="970" r="32"/>
      <path d="M1443 970 L1500 1030" stroke-linecap="round"/>
    </g>
  </g>

  <!-- steps -->
  <g class="steps">
    <path d="M455 928 H633 L672 968 H633 V1270 H133 V1170 H240 V1085 H365 V1000 H455 Z" fill="var(--light-blue)"/>
    <text class="cond-bold" x="620" y="995" font-size="72" fill="var(--white)" text-anchor="end" textLength="132" lengthAdjust="spacingAndGlyphs">small</text>
    <text class="cond-bold" x="327" y="1072" font-size="72" fill="var(--navy)" textLength="30" lengthAdjust="spacingAndGlyphs">&amp;</text>
    <text class="cond-bold" x="372" y="1072" font-size="72" fill="var(--white)" textLength="248" lengthAdjust="spacingAndGlyphs">measured</text>
    <text class="cond-bold" x="262" y="1152" font-size="72" fill="var(--white)" textLength="358" lengthAdjust="spacingAndGlyphs">steps towards</text>
    <rect x="145" y="1180" width="475" height="80" fill="var(--navy)"/>
    <text class="cond-bold" x="382" y="1248" font-size="72" fill="var(--white)" text-anchor="middle" textLength="398" lengthAdjust="spacingAndGlyphs">HIGHER GOALS</text>
  </g>

  <!-- lens -->
  <g class="lens">
    <path d="M760 1150 L575 1395" stroke="var(--blue)" stroke-width="38" stroke-linecap="round"/>
    <circle cx="872" cy="1022" r="150" fill="var(--panel)"/>
    <circle cx="872" cy="1022" r="146" fill="var(--blue)"/>
    <circle cx="872" cy="1022" r="123" fill="var(--white)"/>
    <path d="M749 1008 A123 123 0 0 1 995 1008 Z" fill="var(--yellow)"/>
    <text class="cond-bold" x="872" y="998" font-size="78" fill="var(--ink)" text-anchor="middle" textLength="192" lengthAdjust="spacingAndGlyphs">BROADEN</text>
    <text class="cond-bold" x="872" y="1068" font-size="68" fill="var(--blue)" text-anchor="middle" textLength="92" lengthAdjust="spacingAndGlyphs">our</text>
    <text class="cond-bold" x="872" y="1113" font-size="52" fill="var(--blue)" text-anchor="middle" textLength="142" lengthAdjust="spacingAndGlyphs">LENS</text>
  </g>

  <!-- staff -->
  <g class="staff">
    <path d="M1048 1090 H1450 Q1497 1090 1497 1137 V1283 Q1497 1330 1450 1330 H885 Q838 1330 838 1283 V1175 H1005 Q1018 1090 1048 1090 Z" fill="var(--blue)"/>
    <text class="cond" x="1020" y="1170" font-size="54" fill="var(--white)" textLength="425" lengthAdjust="spacingAndGlyphs">Staff doing what they</text>
    <text class="cond" x="1020" y="1235" font-size="50" fill="var(--white)" textLength="95" lengthAdjust="spacingAndGlyphs">LOVE</text>
    <text class="cond-bold" x="1136" y="1235" font-size="60" fill="var(--yellow)" textLength="315" lengthAdjust="spacingAndGlyphs">Teaching Kids</text>
    <text class="cond-bold" x="1020" y="1295" font-size="60" fill="var(--yellow)" textLength="432" lengthAdjust="spacingAndGlyphs">for proven growth</text>
  </g>

  <!-- partnerships -->
  <g class="partnerships">
    <path d="M828 1215 V1293 Q828 1340 870 1340 H1440 V1420 H820 Q710 1420 710 1310 Z" fill="var(--navy)"/>
    <text class="cond" x="820" y="1395" font-size="54" fill="var(--white)" textLength="268" lengthAdjust="spacingAndGlyphs">Build &amp; value</text>
    <rect x="1108" y="1352" width="322" height="60" fill="var(--yellow)"/>
    <text class="cond-bold" x="1269" y="1403" font-size="52" fill="var(--navy)" text-anchor="middle" textLength="305" lengthAdjust="spacingAndGlyphs">PARTNERSHIPS</text>
    <path d="M920 1422 H1468 V1535 H985 Q920 1535 920 1470 Z" fill="var(--light-blue)"/>
    <text class="cond" x="965" y="1470" font-size="38" fill="var(--white)" textLength="460" lengthAdjust="spacingAndGlyphs">• connect  • celebrate  • strong</text>
    <text class="cond" x="988" y="1512" font-size="38" fill="var(--white)" textLength="462" lengthAdjust="spacingAndGlyphs">• predictable • laugh • have fun</text>
  </g>

  <!-- expectations -->
  <g class="expectations">
    <path d="M147 1336 L367 1386 H147 Z" fill="var(--light-blue)"/>
    <text class="cond-bold" x="143" y="1448" font-size="50" fill="var(--navy)" textLength="244" lengthAdjust="spacingAndGlyphs">communicate</text>
    <text class="cond-bold" x="143" y="1515" font-size="60" fill="var(--blue)" textLength="304" lengthAdjust="spacingAndGlyphs">communicate</text>
    <text class="cond-bold" x="143" y="1582" font-size="68" fill="#111111" textLength="344" lengthAdjust="spacingAndGlyphs">communicate</text>
    <rect x="143" y="1600" width="477" height="83" fill="var(--navy)"/>
    <text class="cond-bold" x="381" y="1672" font-size="76" fill="var(--white)" text-anchor="middle" textLength="438" lengthAdjust="spacingAndGlyphs">EXPECTATIONS</text>
    <text class="cond-bold" x="155" y="1740" font-size="46" fill="var(--blue)" textLength="440" lengthAdjust="spacingAndGlyphs">• SUPPORT  • FOR CLARITY</text>
    <g class="chat-icon" fill="none" stroke="var(--line)" stroke-width="9" stroke-linejoin="round">
      <path d="M490 1805 H445 Q440 1805 440 1815 V1880 Q440 1890 450 1890 H470 V1922 L505 1890 H565"/>
      <path d="M505 1782 H595 Q607 1782 607 1795 V1855 Q607 1865 595 1865 H575 V1895 L545 1865 H505 Q490 1865 490 1850 V1795 Q490 1782 505 1782 Z"/>
    </g>
  </g>

  <!-- wellness -->
  <g class="wellness">
    <path d="M1262 1556 H1428 L1395 1740 L1392 1578 Z" fill="var(--yellow)"/>
    <rect x="833" y="1590" width="495" height="93" fill="var(--blue)"/>
    <text class="cond-bold" x="1080" y="1668" font-size="84" fill="var(--white)" text-anchor="middle" textLength="470" lengthAdjust="spacingAndGlyphs">MENTAL HEALTH</text>
    <rect x="980" y="1670" width="45" height="80" fill="var(--ink)"/>
    <text class="cond-bold" x="1002" y="1735" font-size="56" fill="var(--white)" text-anchor="middle">&amp;</text>
    <rect x="1027" y="1672" width="341" height="80" fill="var(--yellow)"/>
    <text class="cond-bold" x="1197" y="1743" font-size="84" fill="var(--white)" text-anchor="middle" textLength="305" lengthAdjust="spacingAndGlyphs">WELLNESS</text>
    <text class="cond-bold" x="1352" y="1802" font-size="48" fill="var(--navy)" text-anchor="end" textLength="270" lengthAdjust="spacingAndGlyphs">FOR ALL IN OUR</text>
    <text class="cond-bold" x="1352" y="1857" font-size="48" fill="var(--navy)" text-anchor="end" textLength="378" lengthAdjust="spacingAndGlyphs">SCHOOL COMMUNITY</text>
  </g>

  <!-- foundational promises -->
  <g class="promises">
    <text class="cond" x="80" y="2052" font-size="90" fill="var(--navy)" textLength="700" lengthAdjust="spacingAndGlyphs">FOUNDATIONAL PROMISES</text>
    <rect x="810" y="1985" width="732" height="72" fill="var(--navy)"/>
    <text class="cond" x="1176" y="2042" font-size="54" fill="var(--white)" text-anchor="middle" textLength="690" lengthAdjust="spacingAndGlyphs">4 YEARS STRONG. BETTER EVERYDAY</text>
  </g>
</svg>
</body>
</html>
```